Stationery Design for Tierhaven

We already have a logo a Logo for our outstanding veterinary hospital. Now we are looking for our future letterhead, business cards and envelopes. We would like to see a design using the color from our logo. Additional color should be limited to grey or a rusty brown. The font should be easy and clearly readable and must be easily available on all computers (to install it in our Management software). The finial design should communicate competence in veterinary medicine, and empathy.

To meet the European regulation (DIN5008) there are a couple mandatory legal informations one the letterhead. We also enclosed a template of exact measurement, which need to be respected according to DIN5008.

Mandatory legal information are (best placed in the footer):
"Tierhaven GmbH & Co KG, Ostrowgasse 417C, 1230 Wien,
Handelsgericht Wien, FN 924615k, GF: Dr. Lukas Brandl
ATU 3148926"
Additional informations needed:
"Tel: +43 1 5849163, Fax: +43 1 5849164, info@tierhaven-example.at, www. tierhaven-example.at"
bank account informations should be included as well. These are:
"Sparkasse Obergruntal, IBAN: AT 58 1111 2222 3333 4444, BIC: SPKTAT4K817"

The Logo should be in the upper right corner. Below that we need a space for informations regarding the responsible veterinarians. There will be 3-5 Names, each of it consisting of 2 lines (see example below). The Names should be highlighted (larger font) compared to the qualifications in the second line.
Tierärztliche Leitung:
Dr. Lukas Brandl
Diplomate ECVS

The contest was startet on the 2nd of may and the deadline was a day later? Why was that so fast? Did I do something wrong? BR

Target Market(s)

dog and cat owner in Austria as welle as referring veterinarians in Austria

Industry/Entity Type

Veterinary

Contact Information for Business Card

One side: Logo
other side:
Dr. Lukas Brandl
Diplomate ECVS
EBVS Specialist of Small Animal Surgery

Tierhaven GmbH&Co KG
Ostrowgasse 417C
1230 Wien

Tel: +43 1 6210000 DW 102
Fax: +43 1 6210000 DW 999
email: lukas.brandl@tierhaven-example.at

Font styles to use
Serif
Sans Serif

Requirements
Must have
• The logo should be given in the upper right. Most of the legal informations should be given in the footer. The upper left Area should be clear, since the recipient address will be placed there.
Colors should be limited to golden, blue and greyscale (two different gereysacales at most).

```html
<!DOCTYPE html>
<html lang="de">
<head>
<meta charset="utf-8">
<title>Tierhaven Letterhead</title>
<link href="https://fonts.googleapis.com/css2?family=Poppins:wght@400;500;600;700&family=Open+Sans:wght@400;600&family=Great+Vibes&display=swap" rel="stylesheet">
<style>
  :root {
    --stage: #b6b6b6;
    --navy: #1c2656;
    --gold: #e0a928;
    --paper: #ffffff;
    --ink: #2f3036;
    --ink-soft: #8b8c9a;
    --muted: #6d6d72;
    --footer: #414449;
  }
  * { margin: 0; padding: 0; box-sizing: border-box; }
  html, body { width: 1200px; height: 1200px; overflow: hidden; }
  body { background: var(--stage); position: relative; font-family: "Open Sans", sans-serif; }

  .board-title {
    position: absolute; top: 100px; left: 0; width: 1200px; text-align: center;
    font-family: "Poppins", sans-serif; font-weight: 700; font-size: 32px;
    letter-spacing: 3px; color: var(--navy);
  }

  .sheet {
    position: absolute; left: 274px; top: 198px; width: 659px; height: 929px;
    background: var(--paper); box-shadow: 0 2px 10px rgba(0,0,0,.28);
  }

  .brand-band {
    position: absolute; left: 399px; top: 0; width: 260px; height: 66px; background: var(--navy);
  }
  .brand-dot {
    position: absolute; left: 7px; top: 5px; width: 54px; height: 54px; border-radius: 50%;
    background: var(--paper); border: 2px solid var(--gold);
  }
  .brand-name {
    position: absolute; left: 65px; top: 14px; font-family: "Poppins", sans-serif;
    font-weight: 600; font-size: 19px; color: #fff; letter-spacing: -.3px; line-height: 1;
  }
  .brand-tagline {
    position: absolute; left: 65px; top: 37px; font-family: "Poppins", sans-serif;
    font-weight: 500; font-size: 8.6px; color: var(--gold); line-height: 1;
  }

  .letterhead-field {
    position: absolute; right: 296px; top: 68px; font-size: 10.5px; color: var(--muted);
  }

  .vet-board { position: absolute; left: 399px; top: 74px; width: 260px; font-family: "Poppins", sans-serif; }
  .vet-board-title { display: flex; align-items: flex-end; font-weight: 600; font-size: 10.3px; color: var(--navy); }
  .vet-board-title::after { content: ""; flex: 1; border-bottom: 1.2px solid var(--navy); margin: 0 0 3px 1px; }
  .vet { margin-top: 7px; line-height: 1.15; }
  .vet + .vet { margin-top: 7px; }
  .vet-name { font-weight: 600; font-size: 9px; color: #3a3a40; }
  .vet-title { font-family: "Open Sans", sans-serif; font-size: 6.2px; color: var(--navy); }

  .recipient { position: absolute; left: 83px; top: 155px; color: var(--navy); }
  .recipient-label { font-size: 7.5px; }
  .recipient-name { font-weight: 600; font-size: 10.8px; }

  .letter-body { position: absolute; left: 83px; top: 284px; width: 508px; }
  .letter-body p {
    font-size: 10.1px; line-height: 14.4px; text-align: justify; margin-bottom: 14.4px; color: var(--ink);
  }
  .letter-body p.soft { color: var(--ink-soft); }

  .signature { position: absolute; left: 421px; top: 716px; width: 166px; text-align: center; }
  .signature-name { font-family: "Great Vibes", cursive; font-size: 22px; color: var(--ink); height: 34px; }
  .signature-rule { border-top: 1px solid var(--ink); margin-top: 5px; }
  .signature-role { margin-top: 11px; font-size: 8.3px; font-weight: 600; letter-spacing: .6px; color: var(--muted); }

  .contact-line {
    position: absolute; left: 0; top: 839px; width: 659px; text-align: center;
    font-family: "Poppins", sans-serif; font-size: 10.6px; color: var(--ink); white-space: nowrap;
  }
  .contact-line b { font-weight: 600; color: var(--navy); }
  .contact-line .sep { margin: 0 12px; }

  .legal-band {
    position: absolute; left: 0; top: 864px; width: 659px; height: 65px; background: var(--footer);
    padding-top: 9px; text-align: center; font-family: "Poppins", sans-serif;
    font-size: 8.9px; line-height: 14.6px; color: #fff;
  }
  .legal-band b { font-weight: 600; }
</style>
</head>
<body>
  <h1 class="board-title">Revised Letterhead Mockup-1a</h1>

  <div class="sheet">
    <div class="brand-band">
      <span class="brand-dot"></span>
      <span class="brand-name">Tierhaven</span>
      <span class="brand-tagline">Fachklinik für Kleintiere</span>
    </div>

    <div class="letterhead-field">feld für Briefkopf, Form B</div>

    <div class="vet-board">
      <div class="vet-board-title">Tierärztliche Leitung:</div>
      <div class="vet"><div class="vet-name">Dr. Lukas Brandl</div><div class="vet-title">Diplomate ECVS</div></div>
      <div class="vet"><div class="vet-name">Dr. Lukas Brandl</div><div class="vet-title">Diplomate ECVS</div></div>
      <div class="vet"><div class="vet-name">Dr. Lukas Brandl</div><div class="vet-title">Diplomate ECVS</div></div>
      <div class="vet"><div class="vet-name">Dr. Lukas Brandl</div><div class="vet-title">Diplomate ECVS</div></div>
      <div class="vet"><div class="vet-name">Dr. Lukas Brandl</div><div class="vet-title">Diplomate ECVS</div></div>
    </div>

    <div class="recipient">
      <div class="recipient-label">To</div>
      <div class="recipient-name">Paul Weber</div>
    </div>

    <div class="letter-body">
      <p class="soft">Lorem ipsum dolor sit amet, consectetur adipiscing elit. Pellentesque dictum, ante non ullamcorp er convallis, nunc quam blandit metus, ac mollis eros felis a orci. Donec congue, mauris ut pulvinar lobortis, dolor massa feugiat nisi, at tincidunt metus leo vel elit. Proin facilisis semper lobortis. Vivamus augue purus, cursus quis urna non, accumsan pellentesque est. Nulla in iaculis magna, quis aliqu et ex. Cras efficitur metus eget purus euismod facilisis. Proin non metus tincidunt, auctor ipsum a, tempor mi.</p>
      <p>Nulla egestas vulputate risus, ut vestibulum diam commodo id. Mauris ornare libero eu erat portt itor ultrices. Proin sed lectus scelerisque ligula bibendum sagittis ac nec leo. Donec ac accumsan diam, et lobortis mauris.</p>
      <p class="soft">Nulla congue volutpat nisl ac lobortis. Integer dignissim interdum libero, quis feugiat velit pretium at. Phasellus sit amet libero rutrum, feugiat odio et, tempus purus. Cras ultricies, leo at fringilla solli cit udin, leo sapien placerat enim, a rutrum lorem enim ut tortor. Phasellus magna ante, cong ue maximus egestas sit amet, venenatis scelerisque felis.</p>
      <p class="soft">Curabitur vitae urna volutpat, varius velit vehicula, fermentum magna. In maximus metus nunc, nec aliquet justo commodo eget. Nullam rhoncus vehicula gravida. Maecenas non sem at erat lacinia con vallis. Aliquam at lobortis erat.</p>
      <p>Nulla egestas vulputate risus, ut vestibulum diam commodo id. Mauris ornare libero eu erat portt itor ultrices. Proin sed lectus scelerisque ligula bibendum sagittis ac nec leo. Donec ac accumsan diam, et lobortis mauris.</p>
      <p>Nulla congue volutpat nisl ac lobortis. Integer dignissim interdum libero, quis feugiat velit pretium at. Phasellus sit amet libero rutrum, feugiat odio et, tempus purus. Cras ultricies, leo at fringilla solli cit udin, leo sapien placerat enim, a rutrum lorem enim ut tortor. Phasellus magna ante, cong ue maximus egestas sit amet, venenatis scelerisque felis.</p>
    </div>

    <div class="signature">
      <div class="signature-name">Mag Stefan Kogler</div>
      <div class="signature-rule"></div>
      <div class="signature-role">DESIGNATION PLACE HERE</div>
    </div>

    <div class="contact-line">
      <b>Tel:</b> +43 1 5849163<span class="sep">|</span><b>Fax:</b> +43 1 5849164<span class="sep">|</span><b>E-Mail:</b> info@tierhaven-example.at<span class="sep">|</span><b>Website:</b> www.tierhaven-example.at
    </div>

    <div class="legal-band">
      <div><b>Sparkasse Obergruntal, IBAN:</b> AT 58 1111 2222 3333 4444, <b>BIC:</b> SPKTAT4K817</div>
      <div>Tierhaven GmbH &amp; Co KG, Ostrowgasse 417C, 1230 Wien, Handelsgericht Wien, FN 924615k,</div>
      <div><b>GF: Dr. Lukas Brandl ATU 3148926</b></div>
    </div>
  </div>
</body>
</html>
```